Schriftdesign für Shop-Header Bild (Schmuckhandel) / Online-Marketing Material
Zielgruppe
Wir verkaufen Schmuck im Onlineshop mit Herz
Aufgabenstellung
Wir benötigen den vorgegebenen Text in schöner Form, Farbe und Größe harmonisch eingefügt, in unserem Bild.
Folgender Text soll sich schick ins Bild einfügen oder in 3-D vielleicht in Schriftfarbe gold hervorheben:
Mit ganzem Herzen für Sie da!
Ihr Online -Juwelier mit Herz
Siehe auch unser altes Bild mit Text, im Shop, wie es nicht aussehen sollte: www.lindenglanzhof.de

```html
<!DOCTYPE html>
<html lang="de">
<head>
<meta charset="utf-8">
<title>Lindenglanzhof – Ihr Online-Juwelier mit Herz</title>
<link rel="stylesheet" href="https://fonts.googleapis.com/css2?family=Lato:wght@400;700&family=Montserrat+Alternates:wght@400&family=Great+Vibes&family=Handlee&display=swap">
<style>
  :root {
    --red: #d3121c;
    --text-dark: #1d1d1d;
    --text-grey: #6f6f6f;
    --nav-grey: #6a696b;
    --field-grey: #ededed;
    --gold: #e7c768;
    --gold-deep: #a07a26;
    --dot-grey: #c9c9c9;
    --seal-grey: #dcdcdc;
  }
  * { box-sizing: border-box; margin: 0; padding: 0; }
  html, body { width: 1200px; height: 855px; overflow: hidden; background: #fff; }
  body { position: relative; font-family: "Lato", sans-serif; color: var(--text-dark); }

  .brand {
    position: absolute; left: 228px; top: 30px;
    display: flex; align-items: center; gap: 8px;
    font-family: "Lato", sans-serif; font-weight: 700; font-size: 17px; color: var(--red);
  }
  .brand-dot { width: 14px; height: 14px; border-radius: 50%; background: var(--red); }

  .top-links { position: absolute; top: 7px; right: 230px; display: flex; gap: 15px; font-size: 9px; }
  .top-links a { color: var(--text-dark); text-decoration: none; }
  .top-links a.is-active { color: var(--red); }

  .search-label { position: absolute; left: 421px; top: 25px; font-size: 12.5px; display: flex; align-items: center; gap: 8px; }
  .search-label svg { width: 9px; height: 6px; }
  .search-field {
    position: absolute; left: 421px; top: 47px; width: 319px; height: 30px;
    background: var(--field-grey); font-size: 10.5px; color: #8a8a8a;
    padding: 9px 18px;
  }
  .search-field svg { position: absolute; right: 8px; top: 5px; width: 22px; height: 20px; }
  .cart-field {
    position: absolute; left: 783px; top: 48px; width: 187px; height: 30px;
    background: var(--field-grey); font-size: 10.5px; color: #e0747a; padding: 9px 18px;
  }
  .cart-field svg { position: absolute; right: 16px; top: 5px; width: 16px; height: 19px; }

  .main-nav {
    position: absolute; left: 0; top: 104px; width: 1200px; height: 33px;
    background: var(--nav-grey);
    font-family: "Montserrat Alternates", sans-serif; font-size: 12px; color: #fff;
  }
  .main-nav span { position: absolute; top: 9px; white-space: nowrap; }

  .hero {
    position: absolute; left: 0; top: 137px; width: 1200px; height: 298px;
    background: radial-gradient(ellipse at 55% 45%, #f3e6d2 0%, #e3d8cb 40%, #cfcbc8 75%, #bdb9b8 100%);
    box-shadow: 0 8px 14px rgba(0,0,0,.12);
  }
  .hero-title {
    position: absolute; left: 0; width: 1200px; text-align: center;
    font-family: "Great Vibes", cursive; color: var(--gold); font-weight: 400;
    text-shadow: 1px 1px 0 var(--gold-deep), 2px 3px 4px rgba(70,45,10,.55);
  }
  .hero-title--top { top: 12px; font-size: 56px; }
  .hero-title--bottom { top: 205px; font-size: 56px; }

  .trust-seal {
    position: absolute; left: 740px; top: 462px; width: 64px; height: 64px;
    border-radius: 50%; background: var(--seal-grey);
  }
  .dotted-rule { position: absolute; left: 727px; width: 243px; border-top: 3px dotted var(--dot-grey); }

  .benefits { position: absolute; left: 729px; top: 558px; list-style: none; }
  .benefits li { display: flex; align-items: center; gap: 6px; height: 30px; font-size: 12.5px; color: var(--red); }
  .benefits svg { width: 26px; height: 22px; }

  .store-note { position: absolute; left: 230px; top: 535px; font-size: 14.5px; color: var(--text-grey); }
  .store-note small { font-size: 12px; color: #555; }
  .store-banner {
    position: absolute; left: 230px; top: 570px; width: 465px; height: 155px;
    background: linear-gradient(90deg, #222 0%, #2f2f2f 45%, #8c5a2a 70%, #f0a832 80%, #555 100%);
    box-shadow: 0 1px 4px rgba(0,0,0,.35);
  }

  .welcome { position: absolute; left: 230px; top: 770px; font-family: "Handlee", cursive; font-size: 20px; font-weight: 400; color: var(--text-grey); }
  .welcome em { font-style: normal; color: var(--red); }
  .tagline { position: absolute; left: 230px; top: 818px; font-size: 14.5px; font-weight: 700; color: var(--text-grey); }
</style>
</head>
<body>
  <header>
    <div class="brand"><span class="brand-dot"></span>Lindenglanzhof</div>
    <nav class="top-links">
      <a class="is-active" href="#">Startseite</a><a href="#">Anmelden</a><a href="#">Mein Konto</a><a href="#">Newsletter abonnieren</a><a href="#">Kontakt</a>
    </nav>
    <div class="search-label">Nach welchem Artikel suchen Sie?
      <svg viewBox="0 0 10 6"><path d="M0 0h10L5 6z" fill="#d3121c"/></svg>
    </div>
    <div class="search-field">Suchen nach
      <svg viewBox="0 0 22 20"><path d="M11 19 2 10a5 5 0 0 1 9-6 5 5 0 0 1 9 6z" fill="#d3121c"/><circle cx="11" cy="9" r="2.5" fill="none" stroke="#fff" stroke-width="1.4"/><path d="M13 11l2 2" stroke="#fff" stroke-width="1.4"/></svg>
    </div>
    <div class="cart-field">Ihr Warenkorb ist leer.
      <svg viewBox="0 0 16 19"><rect x="0" y="5" width="16" height="14" rx="1" fill="#d3121c"/><path d="M5 5V3a3 3 0 0 1 6 0v2" fill="none" stroke="#d3121c" stroke-width="1.5"/><path d="M8 15 5 12a1.6 1.6 0 0 1 3-2 1.6 1.6 0 0 1 3 2z" fill="#fff"/></svg>
    </div>
    <nav class="main-nav">
      <span style="left:324px">KREUZ-ANHÄNGER</span>
      <span style="left:466px">ANHÄNGER/VERSCH.</span>
      <span style="left:621px">FOTO-MEDAILLONS</span>
      <span style="left:766px">OHRSCHMUCK</span>
      <span style="left:881px">ACCESSOIRES</span>
    </nav>
  </header>

  <section class="hero" role="img" aria-label="Goldener Herzanhänger an Kette auf cremefarbenem Seidenstoff">
    <h1 class="hero-title hero-title--top">Mit ganzem Herzen für Sie da!</h1>
    <p class="hero-title hero-title--bottom">Ihr Online -Juwelier mit Herz</p>
  </section>

  <main>
    <p class="store-note">Besuchen Sie auch unseren VELORIA-Schmuck Store: <small>hier</small></p>
    <div class="store-banner" role="img" aria-label="Werbebanner des Schmuck-Stores: Goldschmelze in der Werkstatt, Hinweis Made in Germany"></div>
    <h2 class="welcome">Herzlich Willkommen im <em>Lindenglanzhof.de</em> Schmuck-Shop</h2>
    <p class="tagline">Ihr Online-Juwelier mit Herz</p>
  </main>

  <aside>
    <div class="trust-seal" role="img" aria-label="Platz für ein Siegel für sicheres Einkaufen"></div>
    <div class="dotted-rule" style="top:535px"></div>
    <ul class="benefits">
      <li><svg viewBox="0 0 26 22"><path d="M13 21 2 10a6 6 0 0 1 11-7 6 6 0 0 1 11 7z" fill="#f4b3b8" stroke="#d3121c" stroke-width="1.2"/></svg>Versand innerhalb von 24 Stunden</li>
      <li><svg viewBox="0 0 26 22"><path d="M13 21 2 10a6 6 0 0 1 11-7 6 6 0 0 1 11 7z" fill="#f4b3b8" stroke="#d3121c" stroke-width="1.2"/></svg>schneller, persönlicher Service</li>
      <li><svg viewBox="0 0 26 22"><path d="M13 21 2 10a6 6 0 0 1 11-7 6 6 0 0 1 11 7z" fill="#f4b3b8" stroke="#d3121c" stroke-width="1.2"/></svg>Kundenzufriedenheit an erster Stelle</li>
      <li><svg viewBox="0 0 26 22"><path d="M13 21 2 10a6 6 0 0 1 11-7 6 6 0 0 1 11 7z" fill="#f4b3b8" stroke="#d3121c" stroke-width="1.2"/></svg>sichere Zahlungsmethoden</li>
    </ul>
    <div class="dotted-rule" style="top:685px"></div>
  </aside>
</body>
</html>
```